Tressel Linkworks Line Card

Hello - We're looking to develop a two sided brochure for our company product lines and capabilities. We're a distributor, value-added reseller, we build cable assemblies and panel assemblies. Looking for a flyer to help tell our story. Our primary market is selling to customers in the off-highway equipment markets. Construction, AG and Specialty Vehicles.

```html
<!DOCTYPE html>
<html lang="en">
<head>
<meta charset="utf-8">
<title>Tressel Linkworks Line Card</title>
<link href="https://fonts.googleapis.com/css2?family=Poppins:wght@400;600;700&display=swap" rel="stylesheet">
<style>
  :root {
    --navy: #18224a;
    --red: #d9232a;
    --red-dark: #8e1216;
    --panel: #e6e6e7;
    --white: #ffffff;
    --ink: #1f2a4f;
  }
  * { box-sizing: border-box; margin: 0; padding: 0; }
  html, body { width: 882px; height: 1200px; overflow: hidden; background: var(--white); }
  body { font-family: "Poppins", sans-serif; color: var(--ink); position: relative; }

  .spread {
    position: absolute; left: 0; top: 306px; width: 1652px; height: 1100px;
    transform: scale(0.5339); transform-origin: 0 0;
  }
  .page { position: absolute; top: 0; width: 810px; height: 1100px; background: var(--white); overflow: hidden; }
  .page-front { left: 0; }
  .page-back { left: 843px; }

  .hero-photo {
    position: absolute; left: 0; top: 0; width: 810px; height: 228px;
    background: linear-gradient(160deg, #6f7276 0%, #3e4146 45%, #7e3036 75%, #2c2e32 100%);
  }
  .logo-arc { position: absolute; left: 0; top: 0; width: 810px; height: 228px; }
  .brand {
    position: absolute; left: 0; width: 810px; top: 130px;
    display: flex; justify-content: center; align-items: center; gap: 12px;
    font-weight: 700; font-size: 40px; line-height: 50px; color: var(--navy);
  }
  .brand .mark { width: 18px; height: 18px; background: var(--red); }

  .title-band {
    position: absolute; left: 0; top: 227px; width: 810px; height: 131px;
    background: var(--navy); color: var(--white); text-align: center;
    display: flex; flex-direction: column; justify-content: center;
    font-weight: 700; font-size: 33px; line-height: 42px; text-transform: uppercase;
  }

  .photo { position: absolute; }
  .photo-fuse {
    left: 0; top: 358px; width: 480px; height: 247px;
    background: linear-gradient(135deg, #c9c2b8 0%, #b23038 35%, #2f3136 65%, #a6a39e 100%);
  }
  .photo-panel {
    left: 0; top: 700px; width: 480px; height: 225px;
    background: linear-gradient(135deg, #d8d8d4 0%, #6b6e72 45%, #c9c7c0 100%);
  }

  .items { list-style: none; font-weight: 400; font-size: 19px; line-height: 27px; color: var(--ink); }
  .items li { display: flex; align-items: center; gap: 5px; white-space: nowrap; }
  .items li::before {
    content: ""; width: 11px; height: 11px; border-radius: 50%; flex: none;
    background: var(--red); box-shadow: 0 0 0 2px rgba(217,35,42,0.25);
  }

  .list-panel {
    position: absolute; left: 480px; top: 358px; width: 330px; height: 247px;
    background: var(--panel); padding: 17px 0 0 18px;
  }
  .red-band {
    position: absolute; left: 0; top: 605px; width: 480px; height: 95px;
    background: linear-gradient(180deg, var(--red) 0%, var(--red-dark) 100%);
    padding: 6px 0 0 42px;
  }
  .red-band .items { color: var(--white); }
  .red-band .items li::before { background: var(--navy); box-shadow: none; }
  .red-rule { position: absolute; left: 480px; top: 605px; width: 330px; height: 4px; background: var(--red); }
  .list-lower { position: absolute; left: 498px; top: 612px; }

  .partners {
    position: absolute; left: 58px; top: 958px; width: 694px;
    display: flex; justify-content: space-between; align-items: center;
    font-weight: 700; font-size: 22px; line-height: 32px; color: var(--navy);
  }
  .partners span { display: flex; align-items: center; gap: 6px; white-space: nowrap; }
  .partners .dot { width: 14px; height: 14px; border-radius: 50%; border: 2px solid var(--navy); }
  .partner-rule { position: absolute; left: 135px; top: 1009px; width: 540px; height: 2px; background: var(--red); }

  .contact { position: absolute; left: 0; top: 1018px; width: 810px; text-align: center; color: var(--navy); font-weight: 600; }
  .contact .address { font-size: 16px; line-height: 24px; }
  .contact .phone { font-size: 17px; line-height: 23px; }
  .contact .fax { color: var(--red); }
  .contact .web { font-size: 17px; letter-spacing: 5px; line-height: 28px; }

  .gallery { position: absolute; left: 54px; top: 384px; width: 701px; height: 663px; }
  .tile { position: absolute; width: 212px; height: 200px; border-radius: 16px; }
  .c1 { left: 0; } .c2 { left: 244px; } .c3 { left: 489px; }
  .r1 { top: 0; } .r2 { top: 234px; } .r3 { top: 463px; }
  .tone-red { background: linear-gradient(135deg, #c8bfb3 0%, #b5323a 40%, #303236 75%, #b0aca5 100%); }
  .tone-blue { background: linear-gradient(135deg, #2a3b6b 0%, #8a8c92 45%, #b33a3f 70%, #3a3c42 100%); }
  .tone-grey { background: linear-gradient(135deg, #d6d6d2 0%, #b7b6b1 50%, #c9a64a 80%, #9d9c98 100%); }
  .tone-wood { background: linear-gradient(135deg, #5f6166 0%, #c9b79a 40%, #b8a385 75%, #6b6d72 100%); }
  .tone-dark { background: linear-gradient(135deg, #d4d3cf 0%, #3b3d42 45%, #8e2a30 75%, #c8c7c2 100%); }
  .tone-black { background: linear-gradient(135deg, #2e3034 0%, #c8b43a 45%, #d8d6d0 100%); }
  .tone-redwire { background: linear-gradient(135deg, #2f3134 0%, #3c7a4c 30%, #c52a31 60%, #2a2c30 100%); }
</style>
</head>
<body>
<div class="spread">

  <main class="page page-front">
    <div class="hero-photo" role="img" aria-label="Close-up photo of a wiring enclosure with terminal blocks and red-sleeved black cables"></div>
    <svg class="logo-arc" viewBox="0 0 810 228" aria-hidden="true">
      <circle cx="405" cy="292" r="227" fill="#ffffff" fill-opacity="0.72"/>
    </svg>
    <div class="brand"><span class="mark"></span>Tressel Linkworks</div>

    <header class="title-band">
      <div>Distribution, Contract Manufacturing</div>
      <div>and System Integration</div>
    </header>

    <div class="photo photo-fuse" role="img" aria-label="Photo of a power distribution block with three mega fuses under a red cover"></div>

    <section class="list-panel">
      <ul class="items">
        <li>Power Distribution Modules</li>
        <li>Circuit Breakers, Fuses</li>
        <li>rocker &amp; Toggle Switches</li>
        <li>CAN Switches</li>
        <li>Battery Disconnects</li>
        <li>Battery Equalizers</li>
        <li>Power Converters</li>
        <li>True Sine Wave Inverters</li>
      </ul>
    </section>

    <section class="red-band">
      <ul class="items">
        <li>Battery Separators</li>
        <li>Interconnect Controllers</li>
        <li>Battery Isolators</li>
      </ul>
    </section>
    <div class="red-rule"></div>

    <div class="photo photo-panel" role="img" aria-label="Photo of an assembled control panel with DIN rail terminals, relays and coiled cable"></div>

    <section class="list-lower">
      <ul class="items">
        <li>On Vehicle &amp; Mobile</li>
        <li>Equipment Display</li>
        <li>HMIs Displays SCADA Software</li>
        <li>HMI + PLC Hybrids</li>
        <li>Automation Cables</li>
        <li>Passive Distributors</li>
        <li>DIN Valve Connectors</li>
        <li>Industrial Ethernet</li>
        <li>Fuse Blocks , Fuse Holders</li>
        <li>Circuit Breakers</li>
        <li>Resettable Fuses</li>
        <li>Fuse Accessories</li>
      </ul>
    </section>

    <div class="partners">
      <span>Varnell</span>
      <span><i class="dot"></i>Quellfuse</span>
      <span>Halvex</span>
      <span>Norvane</span>
      <span>Pellmark Automation</span>
    </div>
    <div class="partner-rule"></div>

    <footer class="contact">
      <div class="address">2840 ORCHARD RIDGE RD. KELDEN, IL 60099</div>
      <div class="phone">(555)010-4020 <span class="fax">FAX : (555) 010-4026</span></div>
      <div class="web">www.tressellinkworks.com</div>
    </footer>
  </main>

  <main class="page page-back">
    <div class="hero-photo" role="img" aria-label="Close-up photo of a wiring enclosure with terminal blocks and red-sleeved black cables"></div>
    <svg class="logo-arc" viewBox="0 0 810 228" aria-hidden="true">
      <circle cx="405" cy="292" r="227" fill="#ffffff" fill-opacity="0.72"/>
    </svg>
    <div class="brand"><span class="mark"></span>Tressel Linkworks</div>

    <header class="title-band">
      <div>Distribution, Contract Manufacturing</div>
      <div>and System Integration</div>
    </header>

    <section class="gallery">
      <div class="tile c1 r1 tone-red" role="img" aria-label="Photo of a fuse distribution block with red cover"></div>
      <div class="tile c2 r1 tone-blue" role="img" aria-label="Photo of an open cabinet with colored wiring and a DIN module"></div>
      <div class="tile c3 r1 tone-grey" role="img" aria-label="Photo of a grey enclosure with terminal strip and yellow connectors"></div>
      <div class="tile c1 r2 tone-red" role="img" aria-label="Photo of a rail of red circuit breakers"></div>
      <div class="tile c2 r2 tone-wood" role="img" aria-label="Photo of a wire harness laid out on a wooden build board"></div>
      <div class="tile c3 r2 tone-dark" role="img" aria-label="Photo of a sealed junction box with coiled cable assembly"></div>
      <div class="tile c1 r3 tone-grey" role="img" aria-label="Photo of a control panel with relays and terminals"></div>
      <div class="tile c2 r3 tone-black" role="img" aria-label="Photo of a terminal strip wired with yellow ferrules"></div>
      <div class="tile c3 r3 tone-redwire" role="img" aria-label="Photo of bundled red wires inside a panel"></div>
    </section>
  </main>

</div>
</body>
</html>
```